4th Generation Family Business Needs a New Card Design!

We are a family owned 4th Generation company. We are based in the Sydney, Australia area and we are desperately in need of a more modern and classy card. We are monumental masons who design, supply & erect lasting memorials throughout cemeteries in Sydney. Our customers are normally in a period of grieving. I have attached logo files that will need to be implemented on the card. Company was established 1935. Australian Owned and Operated. Card needs to be designed to PRINTLY.com specification.

Target Market(s)

Our target market is based upon people that a grieving for family members that have passed away. We also deal with alot of companies that own and operate cemeteries.

Industry/Entity Type

Business

Contact Information for Business Card

Oliver Brantley, Operations Manager, 0417552908, oliver@hollowaystoneworks.com.au
Martin Brantley, Director, 0431906627, martin@hollowaystoneworks.com.au
Phone # 02 9634 2258
Website: www.hollowaystoneworks.com.au
Address: Suite 17, 8 Calloway Lane, East Penrose, Sydney NSW 2290

Font styles to use
Serif
Decorative
Script

Requirements
Must have
• Would like to see the logo nicely implemented with a modern design. Embossed lettering would be a nice additive.

```html
<!DOCTYPE html>
<html lang="en">
<head>
<meta charset="utf-8">
<title>Holloway Stoneworks — Business Card</title>
<link rel="stylesheet" href="https://fonts.googleapis.com/css2?family=Cinzel:wght@700&family=Source+Sans+3:wght@400&display=swap">
<style>
  :root {
    --backdrop-top: #2b2b2b;
    --backdrop-bottom: #050505;
    --card-black: #0a0a0a;
    --card-gold: #ebbf2f;
    --gold: #ebbf2f;
    --ink: #1a1a1a;
    --white: #ffffff;
  }
  * { margin: 0; padding: 0; box-sizing: border-box; }
  html, body { width: 1200px; height: 900px; overflow: hidden; }
  body {
    position: relative;
    background: linear-gradient(180deg, var(--backdrop-top) 0%, #1b1b1b 45%, var(--backdrop-bottom) 100%);
    font-family: "Source Sans 3", "Helvetica Neue", Arial, sans-serif;
  }
  .card {
    position: absolute;
    top: 300px;
    width: 442px;
    height: 272px;
    border-radius: 10px;
  }
  .card--front { left: 152px; background: var(--card-black); }
  .card--back { left: 622px; background: var(--card-gold); }

  .brand-name {
    font-family: "Cinzel", "Times New Roman", serif;
    font-weight: 700;
    text-align: center;
    letter-spacing: 1px;
    line-height: 1.15;
  }
  .card--front .brand-name {
    position: absolute;
    left: 22px; top: 104px;
    width: 176px;
    color: var(--white);
    font-size: 21px;
  }
  .card--back .brand-name {
    position: absolute;
    left: 0; right: 0; top: 120px;
    color: var(--ink);
    font-size: 34px;
  }
  .card--back .brand-name .brand-sub { display: block; font-size: 19px; letter-spacing: 3px; }

  .contacts { position: absolute; left: 215px; top: 30px; color: var(--white); }
  .person + .person { margin-top: 14px; }
  .person-name {
    font-family: "Cinzel", "Times New Roman", serif;
    font-weight: 700;
    color: var(--gold);
    font-size: 16px;
    letter-spacing: 0.4px;
    line-height: 20px;
  }
  .person-name .cap { font-size: 18px; }
  .person-role {
    font-family: "Cinzel", "Times New Roman", serif;
    font-weight: 700;
    font-size: 10.5px;
    letter-spacing: 0.3px;
    line-height: 16px;
    color: #e8e8e8;
  }
  .person-role .cap { font-size: 13px; }
  .line {
    display: flex; align-items: center; gap: 6px;
    font-size: 12.5px; line-height: 16.5px;
  }
  .line svg { width: 9px; height: 9px; flex: none; fill: var(--gold); }
  .company-lines { margin-top: 18px; }
  .company-lines .line { gap: 7px; }

  .address {
    position: absolute; left: 0; right: 0; top: 214px;
    text-align: center; color: var(--ink);
    font-size: 12.5px; line-height: 16px;
  }
</style>
</head>
<body>
  <section class="card card--front">
    <div class="brand-name">Holloway Stoneworks</div>
    <div class="contacts">
      <div class="person">
        <div class="person-name"><span class="cap">O</span>LIVER <span class="cap">B</span>RANTLEY</div>
        <div class="person-role"><span class="cap">O</span>PERATIONS <span class="cap">M</span>ANAGER</div>
        <div class="line"><svg viewBox="0 0 10 10"><path d="M3 0h4a1 1 0 0 1 1 1v8a1 1 0 0 1-1 1H3a1 1 0 0 1-1-1V1a1 1 0 0 1 1-1zm0 1.5v6h4v-6z"/></svg>0417552908</div>
        <div class="line"><svg viewBox="0 0 10 10"><path d="M0 2h10v6H0z M0 2l5 3.5L10 2" /></svg>oliver@hollowaystoneworks.com.au</div>
      </div>
      <div class="person">
        <div class="person-name"><span class="cap">M</span>ARTIN <span class="cap">B</span>RANTLEY</div>
        <div class="person-role"><span class="cap">D</span>IRECTOR</div>
        <div class="line"><svg viewBox="0 0 10 10"><path d="M3 0h4a1 1 0 0 1 1 1v8a1 1 0 0 1-1 1H3a1 1 0 0 1-1-1V1a1 1 0 0 1 1-1zm0 1.5v6h4v-6z"/></svg>0431906627</div>
        <div class="line"><svg viewBox="0 0 10 10"><path d="M0 2h10v6H0z"/></svg>martin@hollowaystoneworks.com.au</div>
      </div>
      <div class="company-lines">
        <div class="line"><svg viewBox="0 0 10 10"><path d="M0 3c2-2 8-2 10 0v1.5H7.5V3.5h-5v1H0z M2 5h6l1.5 4h-9z"/></svg>02 9634 2258</div>
        <div class="line"><svg viewBox="0 0 10 10"><circle cx="5" cy="5" r="5"/></svg>www.hollowaystoneworks.com.au</div>
      </div>
    </div>
  </section>

  <section class="card card--back">
    <div class="brand-name">Holloway<span class="brand-sub">Stoneworks</span></div>
    <p class="address">Suite 17, 8 Calloway Lane, East Penrose,<br>Sydney NSW 2290</p>
  </section>
</body>
</html>
```